a mobile app for beauty salon professional to publish their service and customers to book service

I plan to create an iPhone app (support iPhone 6 and above) that will allow beauty salon professionals (e.g. hair stylist) to publish their service/business with address/geolocation and available time slots, manage their professional profile with photos, and service charges, allow the customers to search services based on locations, and book the service. customer can provide feedback/ratings on the professional's service. a reference website : http://velmo.trimbook.example/booking/

Target Market(s)

beauty and hair salon professionals and customers

Industry/Entity Type

Hair And Beauty

Font styles to use
Sans Serif
Script

Colors

Designer to choose colors to be used in the design.

Requirements
Must have
• === customer features
• - user/customer registration
• - customer browse nearby service using a map view
• - customer browse nearby service using a list view ordered by distance (e.g. km)
• - customer search salon service based on service category, price range, and profressional's rating
• - customer select a service with zoom in details : salon name, service offered, location/address, and a "booking" button
• - customer place booking by specifying service (e.g. simple cut, blow-dry, etc) required, time slot, preferred professional
• - customer payments (paypal/credit card)
• - customer can feedback/rate on the salon professional
• === salon professional features
• - user/professional registration
• - maintain professional profile (private/public), option to upload photos
• - a registered professional can register/maintain shop/business who by default is the owner of the shop/business
• - a shop owner can assign professionals to the shop/business (multiple professional can work in the same location/shop)
• - professional maintain their service and schedule (breaks, holidays, working hours, appointments, service rates)

```html
<!DOCTYPE html>
<html lang="en">
<head>
<meta charset="utf-8">
<title>Velmo's Salon – Log in</title>
<link rel="stylesheet" href="https://fonts.googleapis.com/css2?family=Inter:ital,wght@0,300;0,400;0,600;1,600&display=swap">
<style>
  :root {
    --bg-top: #e6c2c2;
    --bg-mid: #f7a6c6;
    --bg-bottom: #fa63bb;
    --brand: #f0287a;
    --white: #ffffff;
    --ink: #3a3036;
    --line: #5a4550;
    --btn-start: #fd6584;
    --btn-mid: #fb4b8c;
    --btn-end: #fb56c3;
  }
  * { margin: 0; padding: 0; box-sizing: border-box; }
  html, body {
    width: 714px; height: 1200px; overflow: hidden;
    font-family: "Inter", "Helvetica Neue", Arial, sans-serif;
  }
  .screen {
    position: relative; width: 714px; height: 1200px; overflow: hidden;
    background: linear-gradient(180deg, var(--bg-top) 0%, var(--bg-mid) 40%, #f98cc8 70%, var(--bg-bottom) 100%);
  }
  .hero-photo {
    position: absolute; left: 0; top: 0; width: 714px; height: 760px;
    background: radial-gradient(ellipse 55% 60% at 45% 40%, rgba(255,210,220,0.55), rgba(240,170,190,0) 70%),
                linear-gradient(180deg, rgba(210,170,170,0.35), rgba(247,166,198,0));
  }
  .brand { position: absolute; top: 0; left: 0; width: 714px; text-align: center; }
  .brand-mark {
    position: absolute; top: 200px; width: 714px; text-align: center;
    font-size: 72px; font-weight: 300; color: var(--brand); letter-spacing: 1px;
  }
  .brand-name {
    position: absolute; top: 336px; width: 714px; text-align: center;
    font-size: 33px; font-weight: 300; color: var(--white);
  }
  .brand-tagline {
    position: absolute; top: 377px; left: 405px;
    font-size: 11px; font-weight: 600; color: var(--ink);
  }
  .field { position: absolute; left: 166px; width: 381px; border-bottom: 1px solid var(--line); }
  .field-label {
    position: absolute; left: 47px; font-size: 14px; font-weight: 600; font-style: italic; color: var(--white);
  }
  .field-email { top: 512px; height: 48px; }
  .field-email .field-label { top: -24px; }
  .field-email .field-value {
    position: absolute; left: 47px; top: 14px; font-size: 22px; font-weight: 300; color: var(--ink);
  }
  .field-password { top: 600px; height: 45px; }
  .field-password .field-label { top: 22px; }
  .field-icon { position: absolute; left: 3px; }
  .field-email .field-icon { top: 26px; }
  .field-password .field-icon { top: 18px; }
  .toggle-visibility { position: absolute; right: 8px; top: 23px; }
  .forgot-link {
    position: absolute; top: 668px; right: 167px;
    font-size: 14px; font-weight: 600; font-style: italic; color: var(--white);
  }
  .btn-login {
    position: absolute; top: 749px; left: 168px; width: 380px; height: 65px; border-radius: 8px;
    background: linear-gradient(90deg, var(--btn-start), var(--btn-mid) 60%, var(--btn-end));
    box-shadow: 0 14px 24px rgba(230, 60, 120, 0.28);
    color: var(--white); font-size: 34px; font-weight: 300;
    display: flex; align-items: center; justify-content: center;
  }
  .btn-social {
    position: absolute; top: 888px; left: 168px; width: 380px; height: 65px; border-radius: 8px;
    border: 1px solid rgba(255,255,255,0.85);
    color: var(--white); font-size: 17px; font-weight: 300;
    display: flex; align-items: center; justify-content: center;
  }
  .btn-social .social-dot {
    position: absolute; left: 24px; top: 22px; width: 20px; height: 20px; border-radius: 50%;
    background: var(--white);
  }
  .signup-prompt {
    position: absolute; top: 1105px; width: 714px; text-align: center;
    font-size: 17px; font-weight: 300; color: var(--ink);
  }
  .signup-prompt strong { font-weight: 600; color: var(--white); margin: 0 6px; }
</style>
</head>
<body>
<main class="screen">
  <div class="hero-photo" role="img" aria-label="Soft pink-tinted portrait photo of a client with a styled haircut, seen in profile"></div>

  <header class="brand">
    <div class="brand-mark">Velmo</div>
    <h1 class="brand-name">Velmo's Salon</h1>
    <p class="brand-tagline">A Trimbook Pro site</p>
  </header>

  <form class="login-form">
    <div class="field field-email">
      <span class="field-label">Username / Email</span>
      <svg class="field-icon" width="18" height="18" viewBox="0 0 18 18" aria-hidden="true">
        <circle cx="9" cy="5" r="4" fill="#3a3036"/>
        <path d="M1 18c0-5 3.5-8 8-8s8 3 8 8z" fill="#3a3036"/>
      </svg>
      <span class="field-value">velmos@velmossalon.example</span>
    </div>

    <div class="field field-password">
      <svg class="field-icon" width="14" height="18" viewBox="0 0 14 18" aria-hidden="true">
        <path d="M3 8V5a4 4 0 0 1 8 0" fill="none" stroke="#3a3036" stroke-width="2"/>
        <rect x="0" y="8" width="14" height="10" rx="2" fill="#3a3036"/>
      </svg>
      <span class="field-label">Password</span>
      <svg class="toggle-visibility" width="18" height="12" viewBox="0 0 18 12" aria-hidden="true">
        <path d="M1 6C4 1 14 1 17 6 14 11 4 11 1 6z" fill="#3a3036"/>
        <circle cx="9" cy="6" r="3" fill="#f7a6c6"/>
        <circle cx="9" cy="6" r="1.5" fill="#3a3036"/>
      </svg>
    </div>

    <a class="forgot-link">Forgot Password?</a>

    <div class="btn-login">Log in</div>

    <div class="btn-social"><span class="social-dot"></span>Log in with Friendloop</div>
  </form>

  <p class="signup-prompt">New user?<strong>Sign up</strong>here</p>
</main>
</body>
</html>
```